Ridge Contracting LLC Business Card Design

I am looking for a creative and unique business card design. We are a commercial construction general contractor. With the name "RIDGE" Contracting, I am hoping to see some neat designs that correlate with the name.

```html
<!DOCTYPE html>
<html lang="en">
<head>
<meta charset="utf-8">
<title>Ridge Contracting – Business Card</title>
<link rel="stylesheet" href="https://fonts.googleapis.com/css2?family=Barlow+Semi+Condensed:wght@500;600&family=Saira+Condensed:wght@800&display=swap">
<style>
  :root {
    --page: #ffffff;
    --card: #2a2b2c;
    --card-dark: #161718;
    --blue: #2a9be0;
    --blue-deep: #1670b8;
    --silver: #c9cbcd;
    --silver-dim: #8d9093;
    --text: #f2f3f4;
    --rule: #3a3c3e;
  }
  * { margin: 0; padding: 0; box-sizing: border-box; }
  html, body { width: 1200px; height: 800px; overflow: hidden; background: var(--page); }
  .canvas { position: relative; width: 1200px; height: 800px; }

  .card {
    position: absolute;
    left: 244px;
    width: 635px;
    height: 350px;
    background: radial-gradient(ellipse at 50% 40%, var(--card) 0%, var(--card-dark) 100%);
    overflow: hidden;
    box-shadow: 0 6px 14px rgba(0,0,0,0.25);
  }
  .card--front { top: 26px; }
  .card--back { top: 412px; }

  /* Front: name lockup with one plain circle */
  .front-lockup {
    position: absolute;
    inset: 0;
    display: flex;
    align-items: center;
    justify-content: center;
    gap: 26px;
  }
  .front-mark {
    width: 96px; height: 96px; flex: none;
    border-radius: 50%;
    background: var(--silver);
  }
  .front-name {
    display: flex;
    flex-direction: column;
    align-items: flex-start;
    font-family: "Saira Condensed", sans-serif;
    font-weight: 800;
    color: var(--blue);
    line-height: 1;
  }
  .front-name__main { font-size: 124px; letter-spacing: 4px; }
  .front-name__sub { font-size: 34px; letter-spacing: 11.5px; margin-top: -4px; }

  /* Back */
  .back-name {
    position: absolute;
    left: 36px;
    top: 20px;
    display: flex;
    flex-direction: column;
    font-family: "Saira Condensed", sans-serif;
    font-weight: 800;
    color: var(--silver);
    line-height: 1;
  }
  .back-name__main { font-size: 52px; letter-spacing: 2px; }
  .back-name__sub { font-size: 18px; letter-spacing: 6.2px; margin-top: -2px; }

  .back-bands { position: absolute; inset: 0; width: 635px; height: 350px; }

  .rule { position: absolute; left: 0; height: 2px; background: var(--rule); }

  .contact {
    position: absolute;
    left: 34px;
    display: flex;
    align-items: center;
    gap: 16px;
    font-family: "Barlow Semi Condensed", sans-serif;
    font-weight: 500;
    font-size: 21px;
    color: var(--text);
  }
  .contact--phone { top: 118px; font-size: 25px; font-weight: 600; }
  .contact--email { top: 165px; }
  .contact--web { top: 206px; }
  .contact--address { top: 256px; align-items: flex-start; line-height: 26px; }
  .icon {
    width: 30px; height: 30px; flex: none;
    background: var(--blue-deep);
    display: flex; align-items: center; justify-content: center;
  }
  .contact--address .icon { height: 42px; margin-top: 2px; }
  .icon svg { width: 20px; height: 20px; }
</style>
</head>
<body>
<main class="canvas">
  <section class="card card--front" aria-label="Card front">
    <div class="front-lockup">
      <span class="front-mark" aria-hidden="true"></span>
      <div class="front-name">
        <span class="front-name__main">RIDGE</span>
        <span class="front-name__sub">CONTRACTING</span>
      </div>
    </div>
  </section>

  <section class="card card--back" aria-label="Card back">
    <svg class="back-bands" viewBox="0 0 635 350" aria-hidden="true">
      <polygon points="0,100 321,100 330,94 600,94 620,0 635,0 615,94 600,104 0,104" fill="var(--blue)"/>
      <polygon points="330,106 600,106 625,40 635,40 635,112 345,112" fill="var(--silver-dim)"/>
      <polygon points="377,350 535,204 635,204 635,214 545,214 395,350" fill="var(--blue)"/>
      <polygon points="415,350 555,222 635,222 635,246 575,246 450,350" fill="var(--silver-dim)"/>
      <polygon points="480,350 590,258 635,258 635,350" fill="#2c2e30"/>
    </svg>

    <div class="back-name">
      <span class="back-name__main">RIDGE</span>
      <span class="back-name__sub">CONTRACTING</span>
    </div>

    <div class="rule" style="top:157px; width:635px"></div>
    <div class="rule" style="top:199px; width:635px"></div>
    <div class="rule" style="top:245px; width:520px"></div>
    <div class="rule" style="top:318px; width:400px; background:var(--silver-dim)"></div>

    <div class="contact contact--phone">
      <span class="icon"><svg viewBox="0 0 24 24"><path fill="#fff" d="M6.6 10.8a15 15 0 0 0 6.6 6.6l2.2-2.2c.3-.3.7-.4 1-.2 1.1.4 2.3.6 3.6.6.6 0 1 .4 1 1V20c0 .6-.4 1-1 1A17 17 0 0 1 3 4c0-.6.4-1 1-1h3.5c.6 0 1 .4 1 1 0 1.3.2 2.5.6 3.6.1.3 0 .7-.2 1z"/></svg></span>
      <span>(123) 456-7890</span>
    </div>
    <div class="contact contact--email">
      <span class="icon"><svg viewBox="0 0 24 24"><rect x="3" y="6" width="18" height="12" fill="none" stroke="#fff" stroke-width="2"/><path d="M3 6l9 7 9-7" fill="none" stroke="#fff" stroke-width="2"/></svg></span>
      <span>info@ridgecontracting.com</span>
    </div>
    <div class="contact contact--web">
      <span class="icon"><svg viewBox="0 0 24 24" fill="none" stroke="#fff" stroke-width="1.6"><circle cx="12" cy="12" r="8.5"/><ellipse cx="12" cy="12" rx="4" ry="8.5"/><path d="M3.5 12h17M5 8h14M5 16h14"/></svg></span>
      <span>www.ridgecontracting.com</span>
    </div>
    <div class="contact contact--address">
      <span class="icon"><svg viewBox="0 0 24 24"><path fill="#fff" d="M12 2a7 7 0 0 0-7 7c0 5 7 13 7 13s7-8 7-13a7 7 0 0 0-7-7zm0 9.5A2.5 2.5 0 1 1 12 6.5a2.5 2.5 0 0 1 0 5z"/></svg></span>
      <span>1234 Industrial Rd,&nbsp; Suite 100<br>Hometown, USA 12345</span>
    </div>
  </section>
</main>
</body>
</html>
```